Retail Jewelry Business Card Design Project

We are in need of a new business card design for a retail jewelry store. This store is in the business of fine jewelry including but not specific to bridal jewelry, diamonds, designer jewelry and watches.

This store has been in business for 20 years but continues to strive for a modern professional appeal. The main colors use for this business are a royal blue, white and silver.

Target Market(s)

Target market is ages 18-50

Industry/Entity Type

Jewelry

Requirements
Must have
• Sales Person Name
Sales Person Email Address

Store Address
Store Phone
Website

Standard business card size. No odd shapes or sizes.
Nice to have
• Overall modern feel for card.

We have thought that a design with a nice feature of the logo on the back of the card would be nice but open to ideas.
Should not have
• No specific images of jewelry should be used.

```html
<!DOCTYPE html>
<html lang="en">
<head>
<meta charset="utf-8">
<title>Marcel Grant Fine Jewelry – Business Card</title>
<link rel="stylesheet" href="https://fonts.googleapis.com/css2?family=Arimo:wght@400&family=Cormorant+Garamond:wght@600&family=Playfair+Display:ital,wght@1,700&display=swap">
<style>
  :root {
    --royal: #2b3190;
    --royal-text: #2f3493;
    --tab: #6a6fc4;
    --white: #ffffff;
    --silver: #dfe1ea;
    --ink: #2a2a2a;
    --backdrop: #eeeeee;
  }
  * { margin: 0; padding: 0; box-sizing: border-box; }
  html, body { width: 1200px; height: 804px; overflow: hidden; }
  body { background: var(--backdrop); position: relative; }

  .card {
    position: absolute;
    width: 540px;
    height: 309px;
    border-radius: 4px;
    box-shadow: 0 4px 14px rgba(0,0,0,0.15);
    overflow: hidden;
  }

  /* Front: contact side */
  .card-front { left: 50px; top: 80px; background: var(--white); }
  .card-front .brand {
    position: absolute; left: 34px; top: 40px;
    font-family: "Cormorant Garamond", serif; font-weight: 600;
    font-size: 34px; line-height: 1.05; color: var(--royal-text);
  }
  .card-front .rep-name {
    position: absolute; right: 36px; top: 132px;
    font-family: "Playfair Display", serif; font-style: italic; font-weight: 700;
    font-size: 15px; color: var(--royal-text);
  }
  .tab { position: absolute; width: 12px; background: var(--tab); }
  .tab-left { left: 0; top: 190px; height: 90px; border-radius: 0 6px 6px 0; }
  .tab-right { right: 0; top: 112px; height: 46px; border-radius: 6px 0 0 6px; }

  .contact-list {
    position: absolute; left: 36px; top: 184px; list-style: none;
    font-family: "Arimo", sans-serif; font-size: 13px; color: var(--ink);
  }
  .contact-list li { display: flex; align-items: center; height: 20px; }
  .contact-list svg { width: 12px; height: 12px; margin-right: 8px; flex: none; }
  .contact-list .address { display: block; height: auto; line-height: 18px; margin-top: 4px; }

  /* Back: brand side */
  .card-back {
    left: 620px; top: 415px; background: var(--royal);
    display: flex; flex-direction: column; align-items: center; justify-content: center;
  }
  .card-back .brand {
    font-family: "Cormorant Garamond", serif; font-weight: 600;
    font-size: 46px; line-height: 1.05; color: var(--silver); text-align: center;
  }
  .card-back .website {
    margin-top: 48px;
    font-family: "Arimo", sans-serif; font-size: 14px; letter-spacing: 2px; color: var(--silver);
  }
</style>
</head>
<body>

  <section class="card card-front" aria-label="Business card front">
    <div class="brand">Marcel Grant<br>Fine Jewelry</div>
    <div class="rep-name">Daniel Reed Ashford</div>
    <span class="tab tab-right"></span>
    <span class="tab tab-left"></span>
    <ul class="contact-list">
      <li>
        <svg viewBox="0 0 12 12" aria-hidden="true"><circle cx="6" cy="6" r="6" fill="var(--ink)"/><path d="M4 3.2c.4-.3.8-.2 1 .2l.4.8c.1.3 0 .5-.2.7l-.3.3c.3.7.8 1.2 1.5 1.5l.3-.3c.2-.2.4-.3.7-.2l.8.4c.4.2.5.6.2 1-.5.6-1.2.8-2 .4C4.9 7.3 4.4 6.8 3.7 5.3c-.3-.8-.2-1.5.3-2.1z" fill="var(--white)"/></svg>
        555-014-2870
      </li>
      <li>
        <svg viewBox="0 0 12 12" aria-hidden="true"><circle cx="6" cy="6" r="6" fill="var(--ink)"/><rect x="3" y="4" width="6" height="4.2" fill="var(--white)"/><path d="M3 4l3 2.3L9 4" stroke="var(--ink)" stroke-width=".7" fill="none"/></svg>
        daniel@marcelgrantjewelry.com
      </li>
      <li>
        <svg viewBox="0 0 12 12" aria-hidden="true"><circle cx="6" cy="6" r="6" fill="var(--ink)"/><circle cx="6" cy="6" r="3.2" stroke="var(--white)" stroke-width=".8" fill="none"/><path d="M2.8 6h6.4M6 2.8c-1.4 1.8-1.4 4.6 0 6.4M6 2.8c1.4 1.8 1.4 4.6 0 6.4" stroke="var(--white)" stroke-width=".6" fill="none"/></svg>
        www.marcelgrantjewelry.com
      </li>
      <li class="address">2210 Marlow Street<br>Bayport, FL 32490</li>
    </ul>
  </section>

  <section class="card card-back" aria-label="Business card back">
    <div class="brand">Marcel Grant<br>Fine Jewelry</div>
    <div class="website">www.marcelgrantjewelry.com</div>
  </section>

</body>
</html>
```